Brimvale OralNet IT Inc. new website

i need a website for my company which is dedicated to installation and service of computer systems in Dental Offices. I would like for it to encompass a technology feel and professional look. The company deals with all aspects of technology like, Audio Visual, computer systems and networks, Cloud services like data backup, data center. We provide manage services, support and services to Dental Professionals.

Looking for a Technology font but professional look Added Wednesday, April 20, 2016

Target Market(s)

Dental, Dentist

Industry/Entity Type

Dental

Number of Pages Required

5+ page

Font styles to use
Other font styles liked:
• Futuristic or Techy

Colors
0255a3
ec1f27

Requirements
Must have
• Tabs
Nice to have
• Have no idea maybe some suggestion on your part may help
Should not have
• A professional feel but have a techy look

```html
<!DOCTYPE html>
<html lang="en">
<head>
<meta charset="utf-8">
<title>Brimvale OralNet IT Inc.</title>
<link href="https://fonts.googleapis.com/css2?family=Lato:wght@400;700;900&family=Roboto:wght@300;400;500&display=swap" rel="stylesheet">
<style>
:root{
  --blue:#0255a3;
  --blue-dark:#063f7c;
  --text:#444;
  --muted:#8a8a8a;
  --band:#efefef;
  --field:#f5f5f5;
  --line:#c9c9c9;
  --white:#fff;
}
*{box-sizing:border-box;margin:0;padding:0}
html,body{width:1200px;height:2880px;overflow:hidden}
body{font-family:"Roboto",Arial,sans-serif;color:var(--text);background:var(--white);position:relative}
section,header,nav,footer{position:relative;width:1200px}
.abs{position:absolute}
.center{left:0;right:0;text-align:center}
.section-title{font-family:"Roboto",Arial,sans-serif;font-weight:400;font-size:42px;color:var(--blue);letter-spacing:.5px;text-transform:uppercase}
.btn{display:flex;align-items:center;justify-content:center;background:var(--blue);color:var(--white);font-size:21px;text-transform:uppercase;letter-spacing:.3px}

/* header */
.site-header{height:115px}
.brand{left:77px;top:30px;display:flex;align-items:center;gap:14px}
.brand-mark{width:40px;height:40px;background:var(--blue);border-radius:6px}
.brand-name{font-family:"Lato",Arial,sans-serif;font-weight:900;font-size:34px;color:var(--blue)}
.contact-chip{top:29px;display:flex;align-items:center;gap:18px;font-size:17px;color:#555}
.chip-icon{width:54px;height:54px;border-radius:50%;background:var(--blue);display:flex;align-items:center;justify-content:center;flex:none}

/* nav */
.main-nav{height:62px;background:var(--blue)}
.nav-list{left:77px;top:0;height:62px;display:flex;list-style:none}
.nav-list li{height:62px;display:flex;align-items:center;color:var(--white);font-size:16px;text-transform:uppercase;padding:0 23px}
.nav-list li.active{background:var(--blue-dark);padding:0 40px}
.nav-search{right:77px;top:19px}

/* hero */
.hero{height:500px;background:linear-gradient(90deg,#e9ebee 0%,#f6f7f8 45%,#e3e7ec 100%)}
.hero-photo{left:700px;top:0;width:380px;height:500px;background:linear-gradient(180deg,#e4e8ed 0%,#c9d3de 100%)}
.hero-title{left:78px;top:166px;font-family:"Lato",Arial,sans-serif;font-weight:700;font-size:42px;line-height:50px;color:var(--blue)}
.hero-text{left:78px;top:220px;width:710px;font-size:18px;line-height:27px;color:#555}
.hero-btn{left:77px;top:281px;width:236px;height:62px;font-family:"Lato",Arial,sans-serif;font-size:22px}

/* welcome */
.welcome{height:390px}
.welcome .section-title{top:58px}
.welcome-text{left:170px;top:120px;width:860px;font-size:14.5px;line-height:24px;color:var(--muted);text-align:center}
.welcome-btn{left:515px;top:262px;width:170px;height:62px}

/* services */
.services{height:556px;background:var(--band)}
.services .section-title{top:58px}
.service{top:144px;width:340px;height:360px;text-align:center}
.service-icon{position:absolute;left:107px;top:0;width:125px;height:125px;border:2px solid var(--blue);border-radius:50%;display:flex;align-items:center;justify-content:center;background:var(--white)}
.service-icon span{width:58px;height:42px;border-radius:6px;background:linear-gradient(135deg,#8fb4d9,#2f6fae)}
.service-name{position:absolute;left:0;right:0;top:155px;font-size:19px;line-height:25px;color:var(--blue);text-transform:uppercase}
.service-text{position:absolute;left:5px;top:212px;width:330px;font-size:14px;line-height:22px;color:var(--muted)}
.service-btn{position:absolute;left:86px;top:292px;width:168px;height:60px}

/* testimonials */
.testimonials{height:370px}
.testimonials .section-title{top:58px}
.testimonial{top:136px;width:520px;height:140px}
.avatar{left:0;top:0;width:115px;height:115px;border-radius:50%;border:3px solid var(--blue);background:linear-gradient(160deg,#d9c3b3,#8e6f5c)}
.quote{left:135px;top:16px;width:385px;font-size:14.5px;line-height:24px;color:var(--muted);padding-left:25px}
.quote-mark{left:135px;top:12px;font-family:"Lato",Arial,sans-serif;font-weight:900;font-size:26px;color:var(--muted)}
.client-name{left:160px;top:109px;font-size:19px;color:var(--blue);text-transform:uppercase}

/* support */
.support{height:239px;background:var(--band)}
.support .section-title{top:36px}
.support-sub{top:98px;font-size:24px;color:#444}
.support-btn{left:503px;top:138px;width:195px;height:60px}

/* contact */
.contact{height:430px}
.contact .section-title{top:58px}
.field{height:42px;background:var(--field);border:1px solid var(--line);font-size:13.5px;color:var(--muted);padding:12px 14px}
.field-message{left:252px;top:188px;width:696px;height:144px}
.send{left:558px;top:292px;width:84px;height:84px;border-radius:50%;background:radial-gradient(circle,#d5d5d5,#9d9d9d);border:5px solid var(--blue);display:flex;align-items:center;justify-content:center}

/* footer */
.footer-info{height:156px;background:var(--band)}
.info-item{top:50px;display:flex;align-items:center;gap:26px}
.info-icon{width:54px;height:54px;border-radius:50%;display:flex;align-items:center;justify-content:center}
.info-icon.solid{background:var(--blue)}
.info-icon.outline{border:2px solid var(--blue);background:var(--white)}
.info-title{font-size:18px;color:#333;text-transform:uppercase}
.info-line{font-size:15.5px;color:#555;margin-top:4px}
.footer-bar{height:62px;background:var(--blue);display:flex;align-items:center;justify-content:center;font-size:15px;color:#111}
.footer-bar strong{color:var(--white);font-weight:500;margin:0 5px;text-transform:uppercase}
</style>
</head>
<body>

<header class="site-header">
  <div class="abs brand">
    <span class="brand-mark"></span>
    <span class="brand-name">Brimvale OralNet IT</span>
  </div>
  <div class="abs contact-chip" style="left:612px">
    <span class="chip-icon"><svg width="24" height="24" viewBox="0 0 24 24"><path fill="#fff" d="M6.6 10.8a15 15 0 0 0 6.6 6.6l2.2-2.2c.3-.3.7-.4 1-.2 1.1.4 2.3.6 3.6.6.6 0 1 .4 1 1V20c0 .6-.4 1-1 1A17 17 0 0 1 3 4c0-.6.4-1 1-1h3.5c.6 0 1 .4 1 1 0 1.3.2 2.5.6 3.6.1.3 0 .7-.2 1z"/></svg></span>
    <span>+(91) 555 010 2468</span>
  </div>
  <div class="abs contact-chip" style="left:870px">
    <span class="chip-icon"><svg width="24" height="18" viewBox="0 0 24 18"><path fill="#fff" d="M0 2l12 8 12-8V0H0zM0 4.5V18h24V4.5l-12 8z"/></svg></span>
    <span>info@brimvaleoralnet.com</span>
  </div>
</header>

<nav class="main-nav">
  <ul class="abs nav-list">
    <li class="active">Home</li>
    <li>About</li>
    <li style="padding:0 40px">Services</li>
    <li style="padding:0 28px">Support</li>
    <li style="padding:0 28px">Client</li>
    <li style="padding:0 28px">Blog</li>
    <li style="padding:0 28px">Contact</li>
  </ul>
  <svg class="abs nav-search" width="24" height="24" viewBox="0 0 24 24"><circle cx="10" cy="10" r="7" fill="none" stroke="#fff" stroke-width="3"/><path d="M15 15l7 7" stroke="#fff" stroke-width="3.5" stroke-linecap="round"/></svg>
</nav>

<section class="hero">
  <div class="abs hero-photo" role="img" aria-label="Smiling dentist in a white coat with arms crossed, dental clinic softly blurred behind"></div>
  <h1 class="abs hero-title">TECHNOLOGY FOR BEST SERVICES</h1>
  <p class="abs hero-text">Lorem Ipsum is simply dummy text of the printing and typesetting industry. Lorem Ipsum has been the industry's standard dummy text ever since the.</p>
  <div class="abs btn hero-btn">Contact Now Us</div>
</section>

<section class="welcome">
  <h2 class="abs center section-title">Welcome to Brimvale OralNet</h2>
  <p class="abs welcome-text">Lorem Ipsum is simply dummy text of the printing and typesetting industry. Lorem Ipsum has been the industry's standard dummy text ever since the 1500s, when an unknown printer took a galley of type and scrambled it to make a type specimen book. It has survived not only five centuries, but also the leap into electronic typesetting, remaining essentially unchanged. It was popularised in the 1960s with the release of Velmark sheets containing Lorem Ipsum passages, and more recently with desktop publishing software like Quillset Layout including versions of Lorem Ipsum.</p>
  <div class="abs btn welcome-btn">Know More</div>
</section>

<section class="services">
  <h2 class="abs center section-title">Our Services</h2>
  <div class="abs service" style="left:76px">
    <div class="service-icon"><span role="img" aria-label="Audio visual device illustration"></span></div>
    <div class="service-name">Audio Visual</div>
    <p class="service-text">Lorem Ipsum is simply dummy text of the printing and typesetting industry. Lorem Ipsum has been the industry's standard dummy.</p>
    <div class="btn service-btn">Know More</div>
  </div>
  <div class="abs service" style="left:433px">
    <div class="service-icon"><span role="img" aria-label="Computer systems and network illustration"></span></div>
    <div class="service-name">Computer Systems and<br>Networks</div>
    <p class="service-text">Lorem Ipsum is simply dummy text of the printing and typesetting industry. Lorem Ipsum has been the industry's standard dummy.</p>
    <div class="btn service-btn">Know More</div>
  </div>
  <div class="abs service" style="left:790px">
    <div class="service-icon"><span role="img" aria-label="Cloud data backup illustration"></span></div>
    <div class="service-name">Cloud Services of Data<br>Backup</div>
    <p class="service-text">Lorem Ipsum is simply dummy text of the printing and typesetting industry. Lorem Ipsum has been the industry's standard dummy.</p>
    <div class="btn service-btn">Know More</div>
  </div>
</section>

<section class="testimonials">
  <h2 class="abs center section-title">Testimonial</h2>
  <div class="abs testimonial" style="left:79px">
    <div class="abs avatar" role="img" aria-label="Client portrait photo"></div>
    <span class="abs quote-mark">&ldquo;</span>
    <p class="abs quote">Lorem Ipsum is simply dummy text of the printing and typesetting industry. Lorem Ipsum has been the industry's standard dummy text....</p>
    <div class="abs client-name">Client Name</div>
  </div>
  <div class="abs testimonial" style="left:620px">
    <div class="abs avatar" role="img" aria-label="Client portrait photo"></div>
    <span class="abs quote-mark">&ldquo;</span>
    <p class="abs quote">Lorem Ipsum is simply dummy text of the printing and typesetting industry. Lorem Ipsum has been the industry's standard dummy text....</p>
    <div class="abs client-name">Client Name</div>
  </div>
</section>

<section class="support">
  <h2 class="abs center section-title">Support With Us</h2>
  <p class="abs center support-sub">Got unanswered questions? We are Ready to Help You</p>
  <div class="abs btn support-btn">Contact Now</div>
</section>

<section class="contact">
  <h2 class="abs center section-title">Contact Us</h2>
  <div class="abs field" style="left:252px;top:125px;width:218px">Name</div>
  <div class="abs field" style="left:491px;top:125px;width:219px">E-Mail</div>
  <div class="abs field" style="left:730px;top:125px;width:218px">Subject</div>
  <div class="abs field field-message">Message</div>
  <div class="abs send"><svg width="30" height="22" viewBox="0 0 24 18"><path fill="#fff" d="M0 2l12 8 12-8V0H0zM0 4.5V18h24V4.5l-12 8z"/></svg></div>
</section>

<footer>
  <div class="footer-info">
    <div class="abs info-item" style="left:77px">
      <span class="info-icon solid"><svg width="20" height="26" viewBox="0 0 20 26"><path fill="#fff" d="M10 0a10 10 0 0 0-10 10c0 7 10 16 10 16s10-9 10-16A10 10 0 0 0 10 0zm0 14a4 4 0 1 1 0-8 4 4 0 0 1 0 8z"/></svg></span>
      <div><div class="info-title">Brimvale OralNet IT</div><div class="info-line">Lorem ipsum dolor amet simple.</div></div>
    </div>
    <div class="abs info-item" style="left:434px">
      <span class="info-icon outline"><svg width="22" height="22" viewBox="0 0 24 24"><path fill="#0255a3" d="M6.6 10.8a15 15 0 0 0 6.6 6.6l2.2-2.2c.3-.3.7-.4 1-.2 1.1.4 2.3.6 3.6.6.6 0 1 .4 1 1V20c0 .6-.4 1-1 1A17 17 0 0 1 3 4c0-.6.4-1 1-1h3.5c.6 0 1 .4 1 1 0 1.3.2 2.5.6 3.6.1.3 0 .7-.2 1z"/></svg></span>
      <div class="info-line">+(91) 555 010 2468</div>
    </div>
    <div class="abs info-item" style="left:789px">
      <span class="info-icon outline"><svg width="22" height="17" viewBox="0 0 24 18"><path fill="#0255a3" d="M0 2l12 8 12-8V0H0zM0 4.5V18h24V4.5l-12 8z"/></svg></span>
      <div class="info-line">info@brimvaleoralnet.com</div>
    </div>
  </div>
  <div class="footer-bar">&copy; 2016 <strong>Brimvale OralNet IT</strong> All rights reserved.</div>
</footer>

</body>
</html>
```